Design website home page for pathology consulting company

Starting a new consulting company with anatomic pathologists focused on expert diagnosis and second opinions on difficult pathology cases. In the near future we will be incorporating next generation diagnostics for rare diseases of childhood into the business. These include discovery and testing of DNA for mutations.

The company is formed around one of the best known pathologists in the world named Marcus "Buddy" Halvorsen. The name of the company is "BuddyScope"

We had a logo design by Sketchfold - it is great. I will attach file as soon as I have it (contest ending today). Our company is medical, uses microscopes, DNA, probably will focus on childhood diseases but not solely on childhood diseases. we're not particularly conservative, but the customers we want to appeal to include older practicing pathologists as well as patients (sometimes parents) looking for second opinions.

Think a group of expert doctors diagnosing disease through the microscope and through DNA technology, ages ranging from 35-75 all trained by the best pathologist in the world - "Buddy"

We receive glass slides from diseases from patients all over the world from docs who need an expert to tell them what is the diagnosis. So "path to the diagnosis" is also part of the company marketing message.

We want the website design to describe our company but be very simple to find what one is looking for as we will use it as the launch page to:
1) order services
2) check results/reports
3) set up new account
4) speak with one of the pathologists
5) see our test menu
6) access our educational material/webinars

Update - looking for home page design and then finalists will ask for second page design to keep with theme - ok?

Reason: realized this project isn't web design but web home page design - thanks

Reason: Holidays for some in next two weeks

Reason: Hot discussion among collaborators for a few of the submissions. Will provide detail individually this weekend. Thanks so much for all the submissions!

Target Market(s)

Referring pathologists, physicians who want second opinions on pathology disease diagnosis, patients who have had biopsies (either patients themselves or parents of patients), generally high education level

Industry/Entity Type

Marketing

Requirements
Must have
• BuddyScope
Next Generation Pathology Consultants

```html
<!DOCTYPE html>
<html lang="en">
<head>
<meta charset="utf-8">
<title>BuddyScope — Next Generation Pathology Consultants</title>
<link rel="stylesheet" href="https://fonts.googleapis.com/css2?family=Roboto:wght@400;500&family=Oswald:wght@500&family=Kotta+One&display=swap">
<style>
:root{
  --blue:#0a6fb0;
  --blue-dark:#0b4f8a;
  --blue-top:#0888bf;
  --ink:#4a4a4a;
  --ink-soft:#5b5b5b;
  --line:#dcdcdc;
  --band:#ececec;
  --white:#ffffff;
}
*{box-sizing:border-box;margin:0;padding:0}
html,body{width:1182px;height:1200px;overflow:hidden;background:var(--white)}
body{position:relative;font-family:"Roboto",Arial,sans-serif;color:var(--ink)}
.abs{position:absolute}

/* header */
.site-header{left:0;top:0;width:1182px;height:104px;border-top:3px solid var(--blue-top);
  background:linear-gradient(#fdfdfd,#ededed);border-bottom:1px solid #cfcfcf}
.brand{left:129px;top:14px;width:150px}
.brand-row{display:flex;align-items:center;gap:6px}
.brand-dot{width:20px;height:20px;border-radius:50%;background:var(--blue)}
.brand-name{font-family:"Roboto",sans-serif;font-weight:500;font-size:22px;color:var(--blue);letter-spacing:.2px}
.brand-tag{font-size:7.5px;color:#6b6b6b;margin-top:3px;white-space:nowrap}
.account-bar{left:880px;top:0;display:flex;height:31px;border-radius:0 0 4px 4px;overflow:hidden;
  background:linear-gradient(#1a7ec0,#0b4f8a)}
.account-bar a{display:flex;align-items:center;gap:6px;padding:0 12px;color:#fff;font-size:12px;font-weight:500;text-decoration:none}
.account-bar a+a{border-left:1px solid #3a8fcc}
.phone{left:888px;top:54px;display:flex;align-items:center;gap:8px;font-size:20px;color:#555}

/* hero */
.hero-band{left:0;top:104px;width:1182px;height:394px;background:var(--band)}
.hero{left:129px;top:105px;width:923px;height:429px;
  background:radial-gradient(ellipse at 70% 45%,#0f8fa8 0%,#0a4a5a 35%,#061e26 70%,#04141a 100%);
  box-shadow:0 14px 18px -8px rgba(0,0,0,.35)}
.hero-title{left:162px;top:146px;font-family:"Kotta One",Georgia,serif;font-size:60px;line-height:70px;color:#fff;
  text-shadow:0 2px 4px rgba(0,0,0,.5)}
.slide-arrow{top:258px}

/* navigation */
.side-nav{left:129px;top:595px;width:238px}
.side-nav-head{height:38px;border-radius:6px 6px 0 0;background:linear-gradient(#a8a8a8,#8a8a8a);
  display:flex;align-items:center;gap:10px;padding-left:12px;
  font-family:"Oswald",sans-serif;font-size:24px;color:#fff}
.side-nav ul{list-style:none;background:linear-gradient(90deg,#fafafa,#f0f0f0 85%,#fafafa);border-bottom:1px solid var(--line)}
.side-nav li{display:flex;align-items:center;border-bottom:1px solid #e2e2e2;margin:0 5px;font-size:14px;color:#444;padding:0 0 0 40px;position:relative}
.side-nav li::before{content:"›";position:absolute;left:14px;font-size:11px;color:#777}

/* welcome */
.welcome-title{left:397px;top:594px;font-size:34px;color:#555;font-weight:400}
.welcome-title span{color:var(--blue)}
.body-copy{font-size:12.4px;line-height:18px;color:var(--ink-soft);letter-spacing:.35px}
.more{font-size:12.5px;color:var(--blue-dark);text-decoration:underline}
.divider{left:400px;top:724px;width:605px;height:6px;background:radial-gradient(ellipse at center,rgba(0,0,0,.18),rgba(0,0,0,0) 70%)}
.section-title{font-size:18px;color:var(--blue)}

.news{left:827px;top:756px;width:212px;height:147px;border:1px solid #e0e0e0;border-top:2px solid var(--blue);background:#f7f7f7;padding:12px 10px}

/* footer */
.site-footer{left:0;top:950px;width:1182px;height:214px;background:linear-gradient(#0a8bc0,#0b5596)}
.foot-title{font-size:18.5px;color:#fff;font-weight:500}
.foot-list{list-style:none;font-size:12.2px;color:#fff;line-height:24px}
.foot-list li{padding-left:16px;position:relative;line-height:18px;margin-bottom:6px}
.foot-list li::before{content:"›";position:absolute;left:2px}
.foot-sep{width:0;height:162px;border-left:1px dashed rgba(255,255,255,.5)}
.social{list-style:none;width:196px}
.social li{display:flex;align-items:center;gap:14px;height:35px;border-bottom:1px dotted rgba(255,255,255,.6);font-size:12.2px;color:#fff}
.social li:last-child{border-bottom:none}
.social-square{width:18px;height:18px;border-radius:3px;background:#fff}
.email{left:670px;top:1052px;width:213px;height:33px;background:#fff;border-radius:3px;border:1px solid #cfd8df;
  font-size:12.5px;color:#999;padding:8px}
.subscribe{left:670px;top:1099px;width:112px;height:28px;background:#2a2a2a;border-radius:3px;border:1px solid #555;
  color:#fff;font-weight:500;font-size:16px;display:flex;align-items:center;justify-content:center}
.copyright{left:0;top:1172px;width:1182px;text-align:center;font-size:12.5px;color:#333}
</style>
</head>
<body>

<header class="abs site-header">
  <div class="abs brand" style="top:58px">
    <div class="brand-row"><span class="brand-dot"></span><span class="brand-name">BuddyScope</span></div>
    <div class="brand-tag">Next Generation Pathology Consultants</div>
  </div>
  <nav class="abs account-bar">
    <a href="#"><svg width="14" height="14" viewBox="0 0 14 14"><circle cx="7" cy="7" r="5.5" fill="none" stroke="#fff" stroke-width="2"/><path d="M7 7h6" stroke="#fff" stroke-width="2"/></svg>Login</a>
    <a href="#"><svg width="16" height="14" viewBox="0 0 16 14"><path d="M8 1l5 5H10v4H6V6H3z" fill="#fff"/><rect x="1" y="11" width="14" height="2" fill="#fff"/></svg>Register</a>
  </nav>
  <div class="abs phone">
    <svg width="22" height="22" viewBox="0 0 22 22"><circle cx="11" cy="11" r="10" fill="none" stroke="var(--blue)" stroke-width="1.5"/><path d="M8 6c-1 1-1 3 1 6s4 4 5 4l1-2-2-1-1 1c-1-1-2-2-2-3l1-1-1-2z" fill="var(--blue)"/></svg>
    0198-765-432
  </div>
</header>

<div class="abs hero-band"></div>
<div class="abs hero" role="img" aria-label="Glowing cyan DNA double helix on a dark teal background"></div>
<h1 class="abs hero-title">Path<br>To The<br>Diagnosis</h1>
<svg class="abs slide-arrow" style="left:79px" width="32" height="92" viewBox="0 0 32 92"><path d="M32 0L0 46l32 46L22 46z" fill="var(--blue)"/></svg>
<svg class="abs slide-arrow" style="left:1068px" width="32" height="92" viewBox="0 0 32 92"><path d="M0 0l32 46L0 92l10-46z" fill="var(--blue)"/></svg>

<aside class="abs side-nav">
  <div class="side-nav-head">
    <svg width="16" height="16" viewBox="0 0 16 16"><circle cx="8" cy="8" r="7.5" fill="#fff"/><path d="M4.5 6.5h7L8 10.5z" fill="#8a8a8a"/></svg>
    Navigation
  </div>
  <ul>
    <li style="height:40px">Order Services</li>
    <li style="height:40px">Check Results/Reports</li>
    <li style="height:40px">Set Up New Account</li>
    <li style="height:54px;line-height:18px">Speak With One Of The<br>Pathologists</li>
    <li style="height:40px">See Our Test Menu</li>
    <li style="height:56px;line-height:18px">Access Our Educational<br>Material / Webinars</li>
  </ul>
</aside>

<h2 class="abs welcome-title">Welcome to <span>BuddyScope</span></h2>
<p class="abs body-copy" style="left:397px;top:636px;width:632px">Lorem ipsum dolor sit amet, consectetuer adipiscing elit, sed diam nonummy nibh euismod tincidunt ut laoreet dolore magna aliquam erat volutpat. Ut wisi enim ad minim veniam, quis nostrud exerci tation ullamcorper suscipit lobortis nisl ut aliquip ex ea commodo consequat. Duis autem vel eum iriure dolor in hendrerit in vulputate velit esse molestie consequat,</p>
<a class="abs more" style="left:965px;top:697px">Read More</a>
<div class="abs divider"></div>

<h3 class="abs section-title" style="left:398px;top:757px">What We Do...</h3>
<p class="abs body-copy" style="left:400px;top:789px;width:376px">Lorem ipsum dolor sit amet, consectetuer adipiscing elit, sed diam nonummy nibh euismod tincidunt ut laoreet dolore magna aliquam erat volutpat. Ut wisi enim ad minim veniam, quis nostrud exerci tation ullamcorper suscipit lobortis nisl ut aliquip ex ea commodo consequat.</p>
<a class="abs more" style="left:712px;top:878px">Read More</a>

<section class="abs news">
  <h3 class="section-title">Latest News...</h3>
  <div style="display:flex;align-items:center;gap:8px;margin-top:10px;font-size:13.5px;color:var(--blue)">
    <svg width="24" height="22" viewBox="0 0 24 22"><rect x="1" y="3" width="22" height="18" rx="2" fill="#fff" stroke="var(--blue)" stroke-width="2"/><rect x="1" y="3" width="22" height="5" fill="var(--blue)"/><text x="12" y="19" font-size="10" text-anchor="middle" fill="var(--blue)" font-family="Roboto,sans-serif" font-weight="500">7</text></svg>
    Lorem ipsum dolord
  </div>
  <p class="body-copy" style="margin-top:6px;font-size:12px;line-height:16px;letter-spacing:.2px">Lorem ipsum dolordfaaffa sffafvit amet, Lorem ipsum</p>
  <p style="margin-top:10px;text-align:right;font-size:13px;color:var(--blue)">Read More...</p>
</section>

<footer class="abs site-footer">
  <h4 class="abs foot-title" style="left:132px;top:26px">Quick Links</h4>
  <ul class="abs foot-list" style="left:132px;top:69px;width:150px">
    <li>Order Services</li><li>Check Results/Reports</li><li>Set Up New Account</li><li>Speak With One Of The Pathologists</li>
  </ul>
  <ul class="abs foot-list" style="left:284px;top:67px;width:150px">
    <li>See Our Test Menu</li><li>Access Our Educational Material / Webinars</li>
  </ul>
  <div class="abs foot-sep" style="left:441px;top:29px"></div>

  <h4 class="abs foot-title" style="left:455px;top:26px">Follow Us</h4>
  <ul class="abs social" style="left:456px;top:55px">
    <li><span class="social-square"></span>Be a fan on Circlebook</li>
    <li><span class="social-square"></span>Follow us on Chirper</li>
    <li><span class="social-square"></span>Subscribe to Blog</li>
    <li><span class="social-square"></span>Catch us on ViewTube</li>
  </ul>
  <div class="abs foot-sep" style="left:652px;top:29px"></div>

  <h4 class="abs foot-title" style="left:670px;top:26px">Subscribe For Newsletter</h4>
  <p class="abs" style="left:670px;top:60px;width:225px;font-size:11.5px;line-height:17px;color:#fff;font-weight:500">Lorem ipsum dmaruiolor sit afdddamet, consectetur adipiscing elit.</p>
  <div class="abs foot-sep" style="left:901px;top:29px"></div>

  <div class="abs" style="left:916px;top:120px;display:flex;align-items:center;gap:6px">
    <span style="width:18px;height:18px;border-radius:50%;background:#fff;opacity:.85"></span>
    <span style="font-size:21px;font-weight:500;color:#e8eef3">BuddyScope</span>
  </div>
  <p class="abs" style="left:916px;top:146px;font-size:7.5px;color:#e8eef3;white-space:nowrap">Next Generation Pathology Consultants</p>
</footer>
<div class="abs email">Enter your Email address</div>
<div class="abs subscribe">SUBSCRIBE</div>

<p class="abs copyright">© Copyright 2013 buddyscope. All rights reserved.</p>

</body>
</html>
```